Robotic consulting firm needs a Powerpoint Template

I'm looking for a powerpoint template for my consulting business. We are in the robotic field and needs to present project concept or robotic cell layout to the client. I'm looking for a design that is professionnal and using my logo. Our color is purple, but I don't want to overuse the color everywhere, it needs to look professionnal for the engineer field. Color code is 9F35D8

```html
<!DOCTYPE html>
<html lang="en">
<head>
<meta charset="utf-8">
<title>Norvanta – Robotic Consulting Presentation Template</title>
<link href="https://fonts.googleapis.com/css2?family=Poppins:wght@400;500;600&family=Rubik:wght@600;700;800&display=swap" rel="stylesheet">
<style>
:root{
  --purple:#9f35d8;
  --dark:#333335;
  --ink:#1e1e22;
  --body:#5a5a60;
  --paper:#ffffff;
  --soft:#f4f4f6;
  --canvas:#ffffff;
}
*{box-sizing:border-box;margin:0;padding:0}
html,body{width:1200px;height:807px;overflow:hidden;background:var(--canvas)}
body{position:relative;font-family:"Poppins",sans-serif;color:var(--ink)}
.slide{position:absolute;width:350px;height:197px;background:var(--paper);overflow:hidden;box-shadow:0 4px 14px rgba(0,0,0,.16)}
.slide.soft{background:var(--soft)}
.heading{font-family:"Rubik",sans-serif;font-weight:700;color:var(--ink)}
.slide-title{position:absolute;left:0;right:0;top:11px;text-align:center;font-size:10px}
.slide-title::after{content:"";display:block;width:20px;height:1.6px;background:var(--purple);margin:3px auto 0}
.brand{position:absolute;right:6px;top:26px;display:flex;align-items:center;gap:3px;font-family:"Poppins",sans-serif;font-weight:600;font-size:6.5px;letter-spacing:1.3px;color:var(--purple)}
.brand i{display:block;width:5px;height:5px;background:var(--purple)}
.footer{position:absolute;left:5px;right:5px;bottom:5px;height:10px;display:flex;align-items:center;gap:4px;font-size:4.3px;color:#333}
.footer .dot{width:7px;height:7px;border-radius:50%;background:var(--purple)}
.footer .rule{flex:1;height:.5px;background:#c9c9cf;margin:0 4px 0 6px}
.footer .page{background:var(--purple);color:#fff;border-radius:5px;padding:2px 7px;font-size:4px}
.photo{position:absolute}
.hex{clip-path:polygon(50% 0,100% 25%,100% 75%,50% 100%,0 75%,0 25%)}
p.small{font-size:4.4px;line-height:1.75;color:var(--body);text-align:justify}

/* cover */
.cover .photo{inset:0;background:radial-gradient(circle at 62% 40%,#3f6474 0,#4e4036 28%,#2b2a28 55%,#1a1a1b 100%)}
.cover .shade{position:absolute;inset:0;background:linear-gradient(90deg,rgba(20,20,22,.75),rgba(20,20,22,.15))}
.cover .brand-big{position:absolute;left:15px;top:70px;font-weight:600;font-size:9px;letter-spacing:2.4px;color:var(--purple)}
.cover .url{position:absolute;right:6px;top:93px;font-size:5.5px;color:#fff;padding-bottom:3px;border-bottom:.5px solid rgba(255,255,255,.6);padding-left:4px}
.cover h1{position:absolute;left:15px;top:137px;font-size:14.5px;color:#fff;font-weight:800}
.cover .lead{position:absolute;left:16px;top:157px;width:140px;font-size:5.6px;line-height:1.6;color:#eee}

/* index */
.index-grid{position:absolute;left:42px;top:42px;display:grid;grid-template-columns:127px 127px;column-gap:14px;row-gap:6px}
.index-item{height:17px;display:flex;align-items:center;justify-content:space-between;padding:0 9px;font-size:4.4px;color:#fff;box-shadow:0 1px 3px rgba(0,0,0,.2)}
.index-item b{font-weight:600;font-size:4.8px}
.index-item.dark{background:var(--dark)}
.index-item.purple{background:var(--purple)}

/* about */
.about .frame{position:absolute;left:0;top:0}
.about .photo{left:38px;top:42px;width:107px;height:124px;background:linear-gradient(160deg,#b88a4c,#6a7a92 45%,#2f3d58)}
.about h2{position:absolute;left:175px;top:30px;font-size:9.5px}
.about h2::after{content:"";display:block;width:16px;height:1.4px;background:var(--purple);margin-top:2px}
.about p.small{position:absolute;left:175px;top:54px;width:141px}

/* cell layout */
.cell .p1{left:23px;top:15px;width:32px;height:36px;background:linear-gradient(150deg,#c9a272,#5b4a3c)}
.cell .p2{left:80px;top:13px;width:61px;height:70px;background:linear-gradient(150deg,#7fb2d8,#2c4f78)}
.cell .h1{left:42px;top:45px;width:32px;height:36px;background:var(--purple)}
.cell .h2{left:29px;top:73px;width:18px;height:20px;background:var(--purple)}
.cell .h3{left:117px;top:77px;width:47px;height:54px;background:var(--dark)}
.cell .p3{left:37px;top:80px;width:70px;height:80px;background:linear-gradient(150deg,#4e6e84,#8a6a4c 55%,#2c3a4c)}
.cell .h4{left:116px;top:125px;width:18px;height:20px;background:var(--purple)}
.cell .p4{left:104px;top:145px;width:32px;height:36px;background:linear-gradient(150deg,#6a6a70,#252528)}
.cell h2{position:absolute;left:175px;top:42px;font-size:9.3px}
.cell h2::after{content:"";display:block;width:18px;height:1.4px;background:var(--purple);margin-top:4px}
.cell .intro{position:absolute;left:175px;top:65px;width:140px;font-size:5.3px;line-height:1.6;font-weight:600;color:#222}
.cell p.small{position:absolute;left:175px;top:97px;width:140px}

/* process */
.flow .map{position:absolute;left:18px;top:28px;width:316px;height:162px;border-radius:40px;background:radial-gradient(ellipse at 50% 45%,#ececef 0,#f4f4f6 60%,#fff 100%)}
.flow svg{position:absolute;left:0;top:0}
.flow .node{position:absolute;width:60px;height:60px;border-radius:50%;display:flex;flex-direction:column;align-items:center;justify-content:center;text-align:center;color:#fff;padding:0 8px;box-shadow:0 2px 6px rgba(0,0,0,.25)}
.flow .node.dark{background:var(--dark)}
.flow .node.purple{background:var(--purple)}
.flow .node h3{font-size:4.2px;font-weight:600;line-height:1.2;margin-bottom:2px}
.flow .node p{font-size:3.2px;line-height:1.5}
.flow .hub{position:absolute;left:150px;top:158px;width:50px;text-align:center;font-weight:600;font-size:6px;letter-spacing:.8px;color:var(--purple)}

/* specs */
.specs svg{position:absolute;left:0;top:0}
.specs .card-text{position:absolute;width:60px;text-align:center}
.specs .card-text h3{font-size:4px;font-weight:500;line-height:1.2;color:#222}
.specs .card-text p{font-size:3.1px;line-height:1.5;color:#777;margin-top:2px}

/* timeline */
.timeline svg{position:absolute;left:0;top:0}
.timeline .note{position:absolute;width:62px;text-align:center}
.timeline .note h3{font-size:4.6px;font-weight:500;line-height:1.25;color:#222}
.timeline .note p{font-size:3.3px;line-height:1.55;color:#777;margin-top:3px}
.timeline .year{position:absolute;top:100px;width:40px;text-align:center;font-size:5.3px;font-weight:600;color:#fff;line-height:12px}

/* closing */
.closing .photo{inset:0;background:radial-gradient(circle at 40% 45%,#3a3f4a 0,#23252b 40%,#151518 100%)}
.closing .brand-big{position:absolute;left:38px;top:120px;font-weight:600;font-size:15px;letter-spacing:3px;color:var(--purple)}
.closing h2{position:absolute;left:198px;top:44px;font-family:"Rubik",sans-serif;font-weight:800;font-size:13.5px;line-height:1.3;color:#fff}
.closing h2 span{color:var(--purple)}
.closing .rule{position:absolute;left:199px;top:92px;width:26px;height:1.2px;background:var(--purple)}
.closing ul{position:absolute;left:199px;top:108px;list-style:none}
.closing li{display:flex;align-items:center;gap:6px;margin-bottom:9px;color:#fff}
.closing li .ic{width:10px;height:10px;border-radius:50%;background:#fff;display:flex;align-items:center;justify-content:center}
.closing li small{display:block;font-size:3.6px;color:#ddd}
.closing li strong{display:block;font-size:4.6px;font-weight:500}
</style>
</head>
<body>

<!-- Cover -->
<section class="slide cover" style="left:33px;top:52px">
  <div class="photo" role="img" aria-label="Photo of a colourful vintage robot head in a dim landscape"></div>
  <div class="shade"></div>
  <div class="brand-big">NORVANTA</div>
  <div class="url">www.norvanta-robotics.com</div>
  <h1 class="heading">Robotic Consulting Firm</h1>
  <p class="lead">Practical robotic cell design and automation guidance for modern manufacturing teams, from concept to launch.</p>
</section>

<!-- Index -->
<section class="slide" style="left:425px;top:52px">
  <h2 class="heading slide-title">Index</h2>
  <div class="brand"><i></i>NORVANTA</div>
  <div class="index-grid">
    <div class="index-item dark">01. Agenda<b>01</b></div>
    <div class="index-item purple">02. Index<b>02</b></div>
    <div class="index-item purple">02. Introduction<b>03</b></div>
    <div class="index-item dark">04. Project Objectives<b>04</b></div>
    <div class="index-item dark">03. Robotic Cell Layout Overview<b>05</b></div>
    <div class="index-item purple">06. Process Flow<b>06</b></div>
    <div class="index-item purple">04. Technical Specifications<b>07</b></div>
    <div class="index-item dark">08. Project Timeline<b>08</b></div>
    <div class="index-item dark">05. Cost and ROI Analysis<b>09</b></div>
    <div class="index-item purple">10. Benefits and Expected Outcomes<b>10</b></div>
    <div class="index-item purple">06. Next Steps<b>11</b></div>
    <div class="index-item dark">12. Ending<b>12</b></div>
  </div>
  <div class="footer"><span class="dot"></span>www.norvanta.com<span class="rule"></span><span class="page">Page 02</span></div>
</section>

<!-- About -->
<section class="slide about" style="left:817px;top:52px">
  <div class="brand"><i></i>NORVANTA</div>
  <svg class="frame" width="350" height="197" viewBox="0 0 350 197" aria-hidden="true">
    <polygon points="97,33 155.9,67 155.9,135 97,169 38.1,135 38.1,67" fill="none" stroke="#9f35d8" stroke-width="1.6"/>
  </svg>
  <div class="photo hex" role="img" aria-label="Photo of a white humanoid robot working in a factory"></div>
  <h2 class="heading">About Us</h2>
  <p class="small">We are an independent engineering practice focused on industrial robotics. Our team plans, simulates and commissions robotic cells for assembly, welding, packaging and material handling. Each project starts with a clear study of your process, takt time and floor space, followed by a concept layout your engineers can review and challenge. We select hardware from trusted vendors, validate reach and cycle time in simulation, and support installation on site. The result is a cell that is safe, maintainable and ready to scale with production demand.</p>
  <div class="footer"><span class="dot"></span>www.norvanta.com<span class="rule"></span><span class="page">Page 03</span></div>
</section>

<!-- Robotic cell layout -->
<section class="slide cell" style="left:33px;top:307px">
  <div class="brand"><i></i>NORVANTA</div>
  <div class="photo hex p1" role="img" aria-label="Photo of a small robotic kit on a workbench"></div>
  <div class="photo hex p2" role="img" aria-label="Photo of a robot head in a blue digital scene"></div>
  <div class="photo hex h1"></div>
  <div class="photo hex h2"></div>
  <div class="photo hex h3"></div>
  <div class="photo hex p3" role="img" aria-label="Photo of an engineer celebrating beside a robot build"></div>
  <div class="photo hex h4"></div>
  <div class="photo hex p4" role="img" aria-label="Photo of a small robot figure"></div>
  <h2 class="heading">Robotic Cell Layout Overview</h2>
  <p class="intro">A compact cell layout that balances reach, safety zones and operator access for fast, reliable changeovers.</p>
  <p class="small">Each layout is modelled in 3D and checked for robot reach, cycle time and fencing distances. Conveyors, fixtures and tool changers are placed to shorten paths and keep maintenance simple. Operators get clear access points, while guarding and light curtains meet current safety standards.</p>
  <div class="footer"><span class="dot"></span>www.norvanta.com<span class="rule"></span><span class="page">Page 04</span></div>
</section>

<!-- Process flow -->
<section class="slide flow" style="left:425px;top:307px">
  <div class="map" role="img" aria-label="Faint world map in the background"></div>
  <h2 class="heading slide-title">Process Flow</h2>
  <div class="brand"><i></i>NORVANTA</div>
  <svg width="350" height="197" viewBox="0 0 350 197" aria-hidden="true">
    <g fill="none" stroke-width="18">
      <path d="M109 176 A66 66 0 0 1 117.8 143" stroke="#333335"/>
      <path d="M117.8 143 A66 66 0 0 1 175 110" stroke="#9f35d8"/>
      <path d="M175 110 A66 66 0 0 1 229.1 138.1" stroke="#333335"/>
      <path d="M229.1 138.1 A66 66 0 0 1 241 176" stroke="#9f35d8"/>
    </g>
    <g stroke="#222" stroke-width="1" fill="#222">
      <line x1="160" y1="61" x2="196" y2="61"/><circle cx="160" cy="61" r="1.4"/><circle cx="196" cy="61" r="1.4"/>
      <line x1="91" y1="103" x2="103" y2="91"/><circle cx="91" cy="103" r="1.4"/><circle cx="103" cy="91" r="1.4"/>
      <line x1="251" y1="90" x2="264" y2="103"/><circle cx="251" cy="90" r="1.4"/><circle cx="264" cy="103" r="1.4"/>
      <line x1="61" y1="158" x2="60" y2="175"/><circle cx="61" cy="158" r="1.4"/><circle cx="60" cy="175" r="1.4"/>
      <line x1="292" y1="158" x2="293" y2="175"/><circle cx="292" cy="158" r="1.4"/><circle cx="293" cy="175" r="1.4"/>
    </g>
  </svg>
  <div class="hub">NORVANTA</div>
  <div class="node dark" style="left:41px;top:97px"><h3>CONSECTETUR ADIPISCING ELIT</h3><p>Short summary of this project stage and its key deliverables.</p></div>
  <div class="node purple" style="left:99px;top:36px"><h3>CONSECTETUR ADIPISCING ELIT</h3><p>Short summary of this project stage and its key deliverables.</p></div>
  <div class="node dark" style="left:197px;top:36px"><h3>CONSECTETUR ADIPISCING ELIT</h3><p>Short summary of this project stage and its key deliverables.</p></div>
  <div class="node purple" style="left:256px;top:98px"><h3>CONSECTETUR ADIPISCING ELIT</h3><p>Short summary of this project stage and its key deliverables.</p></div>
  <div class="footer"><span class="dot"></span>www.norvanta.com<span class="rule"></span><span class="page">Page 05</span></div>
</section>

<!-- Technical specifications -->
<section class="slide soft specs" style="left:817px;top:307px">
  <h2 class="heading slide-title">Technical Specifications</h2>
  <div class="brand"><i></i>NORVANTA</div>
  <svg width="350" height="197" viewBox="0 0 350 197" aria-hidden="true">
    <defs><filter id="cardShadow" x="-20%" y="-20%" width="140%" height="140%"><feDropShadow dx="0" dy="1" stdDeviation="1.5" flood-opacity=".18"/></filter></defs>
    <g fill="#fff" filter="url(#cardShadow)">
      <rect x="103" y="36" width="68" height="68" rx="11"/>
      <rect x="179" y="36" width="68" height="68" rx="11"/>
      <rect x="103" y="110" width="68" height="68" rx="11"/>
      <rect x="179" y="110" width="68" height="68" rx="11"/>
    </g>
    <path d="M171 104 L133 104 A38 38 0 0 1 171 66 Z" fill="#9f35d8"/>
    <path d="M179 104 L179 66 A38 38 0 0 1 217 104 Z" fill="#333335"/>
    <path d="M171 110 L171 148 A38 38 0 0 1 133 110 Z" fill="#333335"/>
    <path d="M179 110 L217 110 A38 38 0 0 1 179 148 Z" fill="#9f35d8"/>
    <g fill="none" stroke="#fff" stroke-width=".7">
      <path d="M152 86 v-6 M155 86 v-9 M158 86 v-5 M150 87 h10"/>
      <path d="M190 86 v-6 M193 86 v-9 M196 86 v-5 M188 87 h10"/>
      <path d="M152 128 v-6 M155 128 v-9 M158 128 v-5 M150 129 h10"/>
      <path d="M190 128 v-6 M193 128 v-9 M196 128 v-5 M188 129 h10"/>
    </g>
  </svg>
  <div class="card-text" style="left:106px;top:42px"><h3>CONSECTETUR<br>ADIPISCING ELIT</h3><p>Short summary of this specification and its key values.</p></div>
  <div class="card-text" style="left:184px;top:42px"><h3>CONSECTETUR<br>ADIPISCING ELIT</h3><p>Short summary of this specification and its key values.</p></div>
  <div class="card-text" style="left:106px;top:139px"><h3>CONSECTETUR<br>ADIPISCING ELIT</h3><p>Short summary of this specification and its key values.</p></div>
  <div class="card-text" style="left:184px;top:139px"><h3>CONSECTETUR<br>ADIPISCING ELIT</h3><p>Short summary of this specification and its key values.</p></div>
  <div class="footer"><span class="dot"></span>www.norvanta.com<span class="rule"></span><span class="page">Page 06</span></div>
</section>

<!-- Project timeline -->
<section class="slide soft timeline" style="left:33px;top:562px">
  <h2 class="heading slide-title">Project Timeline</h2>
  <div class="brand"><i></i>NORVANTA</div>
  <svg width="350" height="197" viewBox="0 0 350 197" aria-hidden="true">
    <g fill="#9f35d8">
      <polygon points="30,100 80,100 76,112 34,112"/>
      <polygon points="129,100 179,100 175,112 133,112"/>
      <polygon points="229,100 279,100 275,112 233,112"/>
    </g>
    <g fill="#333335">
      <polygon points="85,100 125,100 131,112 79,112"/>
      <polygon points="184,100 224,100 230,112 178,112"/>
      <polygon points="283,100 323,100 329,112 277,112"/>
    </g>
    <g stroke="#222" stroke-width=".8" fill="#222">
      <line x1="105" y1="83" x2="105" y2="99"/><circle cx="105" cy="83" r="1.4"/>
      <line x1="204" y1="83" x2="204" y2="99"/><circle cx="204" cy="83" r="1.4"/>
      <line x1="303" y1="83" x2="303" y2="99"/><circle cx="303" cy="83" r="1.4"/>
      <line x1="55" y1="113" x2="55" y2="129"/><circle cx="55" cy="129" r="1.4"/>
      <line x1="154" y1="113" x2="154" y2="129"/><circle cx="154" cy="129" r="1.4"/>
      <line x1="254" y1="113" x2="254" y2="129"/><circle cx="254" cy="129" r="1.4"/>
    </g>
  </svg>
  <div class="year" style="left:35px">1998</div>
  <div class="year" style="left:85px">2001</div>
  <div class="year" style="left:134px">2004</div>
  <div class="year" style="left:184px">2008</div>
  <div class="year" style="left:234px">2015</div>
  <div class="year" style="left:283px">2023</div>
  <div class="note" style="left:74px;top:41px"><h3>CONSECTETUR<br>ADIPISCING ELIT</h3><p>Short summary of this milestone and what it delivered.</p></div>
  <div class="note" style="left:173px;top:41px"><h3>CONSECTETUR<br>ADIPISCING ELIT</h3><p>Short summary of this milestone and what it delivered.</p></div>
  <div class="note" style="left:272px;top:41px"><h3>CONSECTETUR<br>ADIPISCING ELIT</h3><p>Short summary of this milestone and what it delivered.</p></div>
  <div class="note" style="left:24px;top:137px"><h3>CONSECTETUR<br>ADIPISCING ELIT</h3><p>Short summary of this milestone and what it delivered.</p></div>
  <div class="note" style="left:123px;top:137px"><h3>CONSECTETUR<br>ADIPISCING ELIT</h3><p>Short summary of this milestone and what it delivered.</p></div>
  <div class="note" style="left:223px;top:137px"><h3>CONSECTETUR<br>ADIPISCING ELIT</h3><p>Short summary of this milestone and what it delivered.</p></div>
  <div class="footer"><span class="dot"></span>www.norvanta.com<span class="rule"></span><span class="page">Page 07</span></div>
</section>

<!-- Closing -->
<section class="slide closing" style="left:425px;top:562px">
  <div class="photo" role="img" aria-label="Dark photo of a robot in a workshop with monitors"></div>
  <div class="brand-big">NORVANTA</div>
  <h2>Thank you<br><span>Contact us</span></h2>
  <div class="rule"></div>
  <ul>
    <li><span class="ic"><svg width="6" height="6" viewBox="0 0 24 24"><path fill="#9f35d8" d="M6.6 10.8a15 15 0 0 0 6.6 6.6l2.2-2.2c.3-.3.7-.4 1-.2 1.1.4 2.3.6 3.6.6.6 0 1 .4 1 1V20c0 .6-.4 1-1 1A17 17 0 0 1 3 4c0-.6.4-1 1-1h3.5c.6 0 1 .4 1 1 0 1.3.2 2.5.6 3.6.1.3 0 .7-.2 1z"/></svg></span><div><small>Call Us</small><strong>+1 555 014 2290</strong></div></li>
    <li><span class="ic"><svg width="6" height="6" viewBox="0 0 24 24"><path fill="#9f35d8" d="M3 5h18v14H3zM4 6.5v.4l8 5.2 8-5.2v-.4z"/></svg></span><div><small>Email</small><strong>hello@norvanta.com</strong></div></li>
    <li><span class="ic"><svg width="6" height="6" viewBox="0 0 24 24"><path fill="#9f35d8" d="M12 2a7 7 0 0 0-7 7c0 5 7 13 7 13s7-8 7-13a7 7 0 0 0-7-7zm0 9.5A2.5 2.5 0 1 1 12 6.5a2.5 2.5 0 0 1 0 5z"/></svg></span><div><small>Address</small><strong>1420 Kestrel Avenue, Pasadena, CA 91101</strong></div></li>
  </ul>
</section>

</body>
</html>
```